Local fast-growing company in the service sector

We are looking for a modern business card design, which should also appear on our letterheads

Target Market(s)

Private and industrial sectors

Contact Information for Business Card

Vorname Name
Lindkofer Str. 18
71468 Waiblingen
Tel.: 07163-418259-0
Name@kovaltec-pbz.de

Colors
9d9d9d
919191
aaaaaa

Requirements
Must have
• The logo (file) in silver

```html
<!DOCTYPE html>
<html lang="de">
<head>
<meta charset="utf-8">
<title>KOVALTEC – Visitenkarte</title>
<link rel="stylesheet" href="https://fonts.googleapis.com/css2?family=Montserrat:wght@400;500;600&display=swap">
<style>
  :root {
    --stage: #111111;
    --card: #151515;
    --band-dark: #3a3a3a;
    --band-mid: #4a4a4a;
    --silver: #aaaaaa;
    --silver-mid: #9d9d9d;
    --silver-dark: #919191;
    --text-light: #e6e6e6;
    --white-bar: #d9d9d9;
  }
  html, body {
    margin: 0;
    width: 1200px;
    height: 1000px;
    overflow: hidden;
    background: var(--stage);
  }
  .business-card {
    position: absolute;
    left: 190px;
    top: 250px;
    width: 820px;
    height: 500px;
    border-radius: 24px;
    background: var(--card);
    overflow: hidden;
    font-family: "Montserrat", sans-serif;
  }
  .business-card svg { display: block; }
  .brand-name { font-weight: 600; font-size: 64px; fill: var(--silver); letter-spacing: 2px; }
  .person-name { font-weight: 500; font-size: 34px; fill: var(--silver); }
  .contact-line { font-weight: 400; font-size: 24px; fill: var(--silver-mid); }
  .address-line { font-weight: 400; font-size: 21px; fill: var(--text-light); }
</style>
</head>
<body>
  <div class="business-card">
    <svg width="820" height="500" viewBox="0 0 820 500" xmlns="http://www.w3.org/2000/svg">
      <g class="brand">
        <rect x="60" y="58" width="62" height="62" fill="var(--silver)"/>
        <text class="brand-name" x="140" y="115">KOVALTEC</text>
      </g>

      <polygon class="name-band" points="0,170 400,170 440,225 400,280 0,280" fill="var(--band-dark)"/>
      <text class="person-name" x="50" y="238">Vorname Name</text>

      <polygon class="contact-band" points="430,185 820,185 820,360 480,360 445,300 462,240" fill="var(--band-mid)"/>
      <g class="contact-phone">
        <path d="M480 255 q-6 10 4 20 l4 -4 -4 -5 q-4 -3 0 -7 l3 -3 -4 -4z" fill="var(--silver-mid)"/>
        <text class="contact-line" x="505" y="273">07163-418259-0</text>
      </g>
      <g class="contact-mail">
        <rect x="472" y="300" width="22" height="15" fill="var(--silver-mid)"/>
        <polyline points="472,300 483,309 494,300" fill="none" stroke="var(--band-mid)" stroke-width="2"/>
        <text class="contact-line" x="505" y="316">Name@kovaltec-pbz.de</text>
      </g>

      <g class="address">
        <polygon points="38,322 52,309 66,322 62,322 62,334 42,334 42,322" fill="var(--text-light)"/>
        <text class="address-line" x="76" y="333">Lindkofer Str. 18 71468 Waiblingen</text>
      </g>

      <polygon class="accent-bar" points="560,395 820,395 820,450 540,450 540,415" fill="var(--white-bar)"/>
    </svg>
  </div>
</body>
</html>
```